Pest control

Pest solutions to all residential and commercial sites, the technicians name will be displayed on the back of the card, and a description of his duties: Pest Technician, Termite Inspector,
Termite protection of properties.
The colours will be all white with VORNO and the 1300 582 417 be a blue.
The file with the phone icon is from my web site.
Industry/Entity Type
Residential
Contact Information for Business Card
VORNO PEST SOLUTIONS, 1300 582 417
vorno.com.au
info@vorno.com.au

```html
<!DOCTYPE html>
<html lang="en">
<head>
<meta charset="utf-8">
<title>VORNO Pest Solutions – Business Card</title>
<link rel="stylesheet" href="https://fonts.googleapis.com/css2?family=Arimo:wght@400;700&family=Michroma&display=swap">
<style>
  :root {
    --backdrop: #2c2c2e;
    --card: #f7f7f7;
    --ink: #111111;
    --band: #0c0c0c;
    --brand-blue: #4862ad;
    --divider: #555555;
    --white: #ffffff;
  }
  * { margin: 0; padding: 0; box-sizing: border-box; }
  html, body {
    width: 1200px; height: 817px; overflow: hidden;
    background: var(--backdrop);
  }
  .card {
    position: absolute; left: 100px; top: 123px;
    width: 1000px; height: 571px;
    background: var(--card);
    border-radius: 36px;
    overflow: hidden;
    font-family: "Michroma", "Arial", sans-serif;
    color: var(--ink);
  }
  .brand { position: absolute; left: 62px; top: 62px; font-family: "Arimo", Arial, sans-serif; }
  .brand-name {
    font-size: 92px; font-weight: 700; line-height: 0.9;
    color: var(--brand-blue); letter-spacing: 1px;
  }
  .brand-tagline {
    margin-top: 6px; margin-left: 24px;
    font-size: 27px; font-weight: 400; line-height: 1; color: var(--ink);
  }
  .name-band {
    position: absolute; left: 0; top: 200px; width: 100%; height: 62px;
    background: var(--band); color: var(--white);
    display: flex; align-items: center; padding-left: 62px;
    white-space: nowrap;
  }
  .person-icon { width: 34px; height: 40px; margin-right: 22px; flex: none; }
  .person-name { font-size: 26px; letter-spacing: 1px; }
  .name-sep { width: 3px; height: 32px; background: var(--white); margin: 0 22px; flex: none; }
  .person-role { font-size: 14px; letter-spacing: 1px; }
  .contacts {
    position: absolute; left: 0; top: 262px; width: 100%; height: 210px;
    display: flex;
  }
  .contact {
    flex: 1; display: flex; flex-direction: column; align-items: center;
    padding-top: 36px;
  }
  .contact + .contact { border-left: 3px solid var(--divider); margin: 24px 0 30px; padding-top: 12px; }
  .contact-icon { width: 74px; height: 74px; }
  .contact-text { margin-top: 30px; font-size: 21px; letter-spacing: 1px; color: var(--ink); white-space: nowrap; }
  .contact-text--phone { color: var(--brand-blue); }
  .address-band {
    position: absolute; left: 0; top: 480px; width: 100%; height: 40px;
    background: var(--brand-blue); color: var(--white);
    display: flex; align-items: center; padding-left: 62px;
    font-size: 16px; letter-spacing: 1.5px;
  }
  .pin-icon { width: 20px; height: 26px; margin-right: 16px; }
</style>
</head>
<body>
  <main class="card">
    <div class="brand">
      <div class="brand-name">VORNO</div>
      <div class="brand-tagline">PEST SOLUTIONS</div>
    </div>

    <div class="name-band">
      <svg class="person-icon" viewBox="0 0 34 40" aria-hidden="true">
        <circle cx="17" cy="11" r="9" fill="var(--white)"/>
        <path d="M1 40 C1 28 8 22 17 22 C26 22 33 28 33 40 Z" fill="var(--white)"/>
      </svg>
      <span class="person-name">DANIEL MERCER</span>
      <span class="name-sep"></span>
      <span class="person-role">PEST TECHNICIAN · TERMITE INSPECTOR</span>
    </div>

    <section class="contacts">
      <div class="contact">
        <svg class="contact-icon" viewBox="0 0 74 74" aria-hidden="true">
          <circle cx="37" cy="37" r="37" fill="var(--brand-blue)"/>
          <rect x="26" y="16" width="22" height="42" rx="4" fill="none" stroke="var(--white)" stroke-width="3"/>
          <line x1="26" y1="23" x2="48" y2="23" stroke="var(--white)" stroke-width="2"/>
          <line x1="26" y1="50" x2="48" y2="50" stroke="var(--white)" stroke-width="2"/>
          <circle cx="37" cy="54" r="1.8" fill="var(--white)"/>
        </svg>
        <span class="contact-text contact-text--phone">1300 582 417</span>
      </div>
      <div class="contact">
        <svg class="contact-icon" viewBox="0 0 74 74" aria-hidden="true">
          <circle cx="37" cy="37" r="37" fill="var(--brand-blue)"/>
          <rect x="18" y="24" width="38" height="26" fill="var(--white)"/>
          <path d="M18 24 L37 40 L56 24" fill="none" stroke="var(--brand-blue)" stroke-width="2.5"/>
          <path d="M18 50 L31 36 M56 50 L43 36" stroke="var(--brand-blue)" stroke-width="2"/>
        </svg>
        <span class="contact-text">info@vorno.com.au</span>
      </div>
      <div class="contact">
        <svg class="contact-icon" viewBox="0 0 74 74" aria-hidden="true">
          <circle cx="37" cy="37" r="37" fill="var(--brand-blue)"/>
          <g fill="none" stroke="var(--white)" stroke-width="2.5">
            <circle cx="37" cy="37" r="18"/>
            <ellipse cx="37" cy="37" rx="8" ry="18"/>
            <line x1="19" y1="37" x2="55" y2="37"/>
            <path d="M22 28 H52 M22 46 H52"/>
            <line x1="37" y1="19" x2="37" y2="55"/>
          </g>
        </svg>
        <span class="contact-text">www.vorno.com.au</span>
      </div>
    </section>

    <div class="address-band">
      <svg class="pin-icon" viewBox="0 0 20 26" aria-hidden="true">
        <path d="M10 0 C4.5 0 0 4.5 0 10 C0 17 10 26 10 26 C10 26 20 17 20 10 C20 4.5 15.5 0 10 0 Z" fill="var(--white)"/>
        <circle cx="10" cy="10" r="3.5" fill="var(--brand-blue)"/>
      </svg>
      <span class="address-text">27 Kestrel Lane, Level 4, Brindale NSW</span>
    </div>
  </main>
</body>
</html>
```